Wander Main Street Merchants Pinebrook Event

We are hosting a Wander Main Street Merchants Pinebrook event in conjunction with Northwind Credit's Hometown Harvest Weekend. Participants will be given a passport to get stamped at participating businesses. They will be entered to win $$ prizes! I have attached a Word document with the info that needs to be included.

Target Market(s)

Christmas shoppers, mainly women.

Colors
f04a50
31b7a3

Requirements
Must have
• The info attached. Christmas or holiday images.

```html
<!DOCTYPE html>
<html lang="en">
<head>
<meta charset="utf-8">
<title>Wander Main Street Merchants Pinebrook – Event Flyer</title>
<link rel="stylesheet" href="https://fonts.googleapis.com/css2?family=Roboto+Slab:wght@400;600&family=Montserrat:wght@500;600;700&display=swap">
<style>
  :root {
    --brand-red: #f04a50;
    --brand-teal: #31b7a3;
    --ink: #2b2b2b;
    --paper: #fbfbfa;
    --stage: #ececec;
    --photo-green: #1f3a2c;
    --photo-brown: #5a3a2a;
    --logo-green: #3f7a52;
    --white: #ffffff;
  }
  * { margin: 0; padding: 0; box-sizing: border-box; }
  html, body { width: 1200px; height: 923px; overflow: hidden; }
  body { background: var(--stage); position: relative; font-family: "Montserrat", sans-serif; }

  .flyer {
    position: absolute; left: 289px; top: 21px;
    width: 622px; height: 880px;
    background: var(--paper);
    box-shadow: 0 10px 30px rgba(0,0,0,.18);
    overflow: hidden;
  }
  .street-photo {
    position: absolute; left: 0; top: 0; width: 622px; height: 560px;
    background:
      linear-gradient(180deg, rgba(255,255,255,.12) 0%, rgba(0,0,0,0) 30%, rgba(10,25,18,.55) 100%),
      linear-gradient(90deg, var(--photo-green) 0%, #3a4a34 50%, var(--photo-brown) 100%);
  }
  .torn-edge { position: absolute; left: 0; top: 540px; width: 622px; height: 30px; }

  .ribbon { position: absolute; left: 186px; top: 118px; width: 250px; height: 50px; }
  .ribbon-text {
    position: absolute; left: 186px; top: 124px; width: 250px; text-align: center;
    font-family: "Roboto Slab", serif; font-weight: 600; font-variant: small-caps;
    font-size: 22px; color: var(--white); letter-spacing: .5px;
  }
  .event-title {
    position: absolute; left: 0; top: 182px; width: 622px; text-align: center;
    font-family: "Roboto Slab", serif; font-weight: 400; color: var(--white);
    font-size: 74px; line-height: 84px; letter-spacing: 3px;
    text-shadow: 0 2px 6px rgba(0,0,0,.35);
  }

  .info-grid { position: absolute; left: 44px; top: 370px; width: 534px; height: 128px; }
  .info-date, .info-time {
    position: absolute; top: 0; font-weight: 700; font-size: 19px; color: var(--white);
  }
  .info-date { left: 10px; }
  .info-date sup { font-size: 9px; }
  .info-time { left: 292px; }
  .dash-h { position: absolute; left: 0; width: 534px; border-top: 2px dashed rgba(255,255,255,.85); }
  .dash-h.top { top: 38px; }
  .dash-h.bottom { top: 126px; }
  .dash-v { position: absolute; left: 267px; top: 0; height: 126px; border-left: 2px dashed rgba(255,255,255,.85); }
  .contact {
    position: absolute; left: 0; top: 40px; width: 265px; height: 84px;
    background: rgba(20,30,24,.45); text-align: center; color: var(--white);
    font-weight: 500; font-size: 15px; line-height: 19px; padding-top: 8px;
  }
  .contact-phone { display: block; margin-top: 4px; color: var(--brand-red); font-weight: 700; font-size: 21px; line-height: 24px; }
  .eligibility {
    position: absolute; left: 280px; top: 50px; width: 250px; text-align: center;
    color: var(--white); font-weight: 500; font-size: 12.5px; line-height: 15px;
  }

  .perks { position: absolute; left: 0; top: 520px; width: 622px; height: 200px; }
  .perk { position: absolute; top: 0; width: 190px; text-align: center; }
  .perk-icon {
    display: block; margin: 0 auto; width: 96px; height: 96px; border-radius: 50%;
    border: 5px solid var(--white); box-shadow: 0 2px 8px rgba(0,0,0,.15);
  }
  .perk-icon.red { background: var(--brand-red); }
  .perk-icon.teal { background: var(--brand-teal); }
  .perk-icon svg { width: 86px; height: 86px; display: block; }
  .perk-text { margin-top: 8px; font-weight: 700; font-size: 13.5px; line-height: 17px; color: var(--ink); }
  .perk-text em { font-style: italic; color: var(--brand-red); }
  .perk.gift { left: 22px; }
  .perk.photo { left: 216px; }
  .perk.prize { left: 410px; }
  .perk-divider { position: absolute; top: 100px; height: 80px; border-left: 2px dashed #555; }
  .perk-divider.one { left: 216px; }
  .perk-divider.two { left: 406px; }

  .sponsors { position: absolute; left: 24px; top: 728px; width: 574px; }
  .sponsor-rule { height: 2px; background: var(--brand-teal); }
  .sponsor-label {
    position: absolute; left: 211px; top: -10px; width: 152px; height: 22px;
    background: var(--brand-teal); color: var(--white); text-align: center;
    font-family: "Roboto Slab", serif; font-variant: small-caps; font-weight: 600; font-size: 13px; line-height: 22px;
  }
  .sponsor-list {
    margin-top: 20px; text-align: center; font-weight: 600; font-size: 8.2px; line-height: 15px; color: var(--ink);
  }
  .sponsor-list .sep { color: var(--brand-red); padding: 0 5px; }
  .sponsor-rule.bottom { margin-top: 12px; }

  .brand-mark {
    position: absolute; left: 0; top: 838px; width: 622px; text-align: center;
    font-family: "Roboto Slab", serif; font-weight: 400; font-size: 24px; color: var(--logo-green); letter-spacing: 1px;
  }
</style>
</head>
<body>
  <article class="flyer">
    <div class="street-photo" role="img" aria-label="Holiday shoppers walking along a busy downtown shopping street"></div>
    <svg class="torn-edge" viewBox="0 0 622 30" preserveAspectRatio="none" aria-hidden="true">
      <path fill="#fbfbfa" d="M0 14 L18 10 L30 16 L52 8 L70 15 L95 11 L112 18 L140 9 L160 14 L188 7 L205 16 L232 12 L255 18 L280 9 L302 15 L330 10 L350 17 L378 8 L400 14 L425 11 L448 18 L470 9 L495 15 L520 8 L540 16 L565 11 L590 17 L610 10 L622 13 L622 30 L0 30 Z"/>
    </svg>

    <svg class="ribbon" viewBox="0 0 250 50" aria-hidden="true">
      <path fill="#c8353b" d="M0 12 L28 12 L28 46 L0 46 L10 29 Z"/>
      <path fill="#c8353b" d="M250 12 L222 12 L222 46 L250 46 L240 29 Z"/>
      <path fill="#f04a50" d="M18 4 Q125 -4 232 4 L232 40 Q125 32 18 40 Z"/>
    </svg>
    <div class="ribbon-text">Wander Main Street</div>

    <h1 class="event-title">MERCHANTS<br>PINEBROOK</h1>

    <section class="info-grid">
      <div class="info-date">27<sup>TH</sup> NOVEMBER 2021</div>
      <div class="info-time">10:00 a.m. – 2:00 p.m.</div>
      <div class="dash-h top"></div>
      <div class="dash-v"></div>
      <div class="contact">For more information,<br>contact Clara Benton<span class="contact-phone">555-014-2290</span></div>
      <p class="eligibility">Eligible to be entered to win when stamps from all participating stores reflected on Wander Main Street Merchants Passport</p>
      <div class="dash-h bottom"></div>
    </section>

    <section class="perks">
      <div class="perk gift">
        <span class="perk-icon red">
          <svg viewBox="0 0 86 86" aria-hidden="true" fill="none" stroke="#fff" stroke-width="3" stroke-linejoin="round">
            <rect x="24" y="36" width="38" height="28"/><rect x="21" y="28" width="44" height="9"/>
            <path d="M43 28 V64"/><path d="M43 28 C36 18 26 20 32 28 M43 28 C50 18 60 20 54 28"/>
          </svg>
        </span>
        <p class="perk-text">Enter to win <em>$500</em><br>in Shopping Dollars<br>and other gift<br>giveaways!</p>
      </div>
      <div class="perk-divider one"></div>
      <div class="perk photo">
        <span class="perk-icon teal">
          <svg viewBox="0 0 86 86" aria-hidden="true" fill="none" stroke="#fff" stroke-width="3" stroke-linejoin="round">
            <path d="M22 32 H33 L37 26 H49 L53 32 H64 V60 H22 Z"/><circle cx="43" cy="45" r="9"/>
          </svg>
        </span>
        <p class="perk-text">Get your pictures<br>with Pinebrook’s<br>Santa Claus.</p>
      </div>
      <div class="perk-divider two"></div>
      <div class="perk prize">
        <span class="perk-icon red">
          <svg viewBox="0 0 86 86" aria-hidden="true" fill="none" stroke="#fff" stroke-width="3" stroke-linecap="round">
            <circle cx="43" cy="43" r="20"/>
            <path d="M50 35 C48 31 36 31 36 38 C36 45 50 41 50 49 C50 55 38 55 36 51 M43 28 V58"/>
          </svg>
        </span>
        <p class="perk-text">Enter to win ONE of<br>FIVE <em>$250</em> Shopping<br>Dollars! Pick up your<br>FREE Tote &amp; Passport<br>at the Depot.</p>
      </div>
    </section>

    <footer class="sponsors">
      <div class="sponsor-rule"></div>
      <div class="sponsor-label">Sponsored By</div>
      <p class="sponsor-list">
        Friday Lantern Nights<span class="sep">|</span>Oakridge Apple Fair<span class="sep">|</span>Birchwood Creative Studio<span class="sep">|</span>Hollis County Chamber &amp; Visitors<br>
        Ivy Lane Photography<span class="sep">|</span>Riverbend Power Cooperative<span class="sep">|</span>Pinebrook Downtown Partners<br>
        The Pinebrook Courier<span class="sep">|</span>Pinebrook’s Santa Claus<span class="sep">|</span>Maple 98.7 FM/AM 1210
      </p>
      <div class="sponsor-rule bottom"></div>
    </footer>

    <div class="brand-mark">Downtown Pinebrook</div>
  </article>
</body>
</html>
```